Luz del Alba(the dawnlite)

We are a Christian Salsa Band in Chicago named Orquesta VELA (orchestra sail). We are done with our single and we need a design for our CD cover. not anything specific just want something nice and I need it yesterday.

Christian

```html
<!DOCTYPE html>
<html lang="es">
<head>
<meta charset="utf-8">
<title>Orquesta VELA – Luz del Alba</title>
<link rel="stylesheet" href="https://fonts.googleapis.com/css2?family=Cinzel:wght@500&family=Arimo:wght@400&display=swap">
<style>
  :root {
    --frame-black: #0c0c0c;
    --frame-white: #ffffff;
    --sky-top: #fbf9f6;
    --sky-mid: #e2d4c3;
    --sky-warm: #c9ab8a;
    --ground: #9c7a58;
    --name-ink: #1a1410;
    --title-fill: #efe7da;
    --title-edge: #1e1812;
  }
  html, body {
    margin: 0;
    padding: 0;
    width: 1200px;
    height: 1200px;
    overflow: hidden;
    background: var(--frame-white);
  }
  .cover {
    position: relative;
    width: 1200px;
    height: 1200px;
    box-sizing: border-box;
    border: 5px solid var(--frame-black);
    background: var(--frame-white);
  }
  .cover__scene {
    position: absolute;
    left: 20px;
    top: 20px;
    right: 20px;
    bottom: 20px;
    background:
      radial-gradient(ellipse 70% 45% at 95% 40%, rgba(255,255,255,0.55), rgba(255,255,255,0) 70%),
      linear-gradient(180deg, var(--sky-top) 0%, var(--sky-mid) 30%, var(--sky-warm) 62%, var(--ground) 100%);
  }
  .band-name {
    position: absolute;
    left: 100px;
    top: 418px;
    margin: 0;
    font-family: "Cinzel", serif;
    font-weight: 500;
    font-size: 92px;
    letter-spacing: 4px;
    line-height: 1;
    color: var(--name-ink);
    white-space: nowrap;
  }
  .single-title {
    position: absolute;
    left: 180px;
    top: 522px;
    margin: 0;
    font-family: "Arimo", sans-serif;
    font-weight: 400;
    font-size: 68px;
    letter-spacing: 3px;
    line-height: 1;
    color: var(--title-fill);
    -webkit-text-stroke: 2px var(--title-edge);
    text-shadow: 4px 5px 6px rgba(40, 28, 18, 0.55);
    white-space: nowrap;
  }
</style>
</head>
<body>
  <main class="cover">
    <div class="cover__scene" role="img" aria-label="Soft sunrise light rays streaming over a blurred city skyline with warm golden bokeh"></div>
    <h1 class="band-name">ORQUESTA VELA</h1>
    <h2 class="single-title">Luz del Alba</h2>
  </main>
</body>
</html>
```